Business Card Design Project

I help solve problems that people have with real estate, so I buy homes for cash that they no longer want, can't afford, inherited, etc. and fix and sell them or rent them or take over mortgage payments. See website: www.quickdeedhomestead.com

Industry/Entity Type

Real Estate

Contact Information for Business Card

Not exactly sure. Looking for a design that either is similar to the website www.quickdeedhomestead.com or that reflects what I do as described below. If it can look a little luxurious to show I can buy the houses for cash and I fix them and sell them, it's a bonus. I seem to like some of the higher end things like foil or black or something that makes it stand out.

Font styles to use
Serif

Requirements
Nice to have
• I seem to like black or clear. I like things to stand out and be different.

```html
<!DOCTYPE html>
<html lang="en">
<head>
<meta charset="utf-8">
<title>Renewed Residences – Business Cards</title>
<link rel="stylesheet" href="https://fonts.googleapis.com/css2?family=Lato:wght@400;700;900&family=Arimo:wght@400;700&display=swap">
<style>
  :root {
    --green-light: #7cbf43;
    --green: #5fa23a;
    --green-deep: #3f8a2a;
    --ink: #1b1b1b;
    --grey-text: #333333;
    --paper: #ffffff;
    --backdrop: #ecebe7;
  }
  * { box-sizing: border-box; margin: 0; padding: 0; }
  html, body { width: 1200px; height: 900px; overflow: hidden; }
  body {
    background: var(--backdrop);
    position: relative;
    font-family: "Lato", sans-serif;
  }
  .card {
    position: absolute;
    left: 280px;
    width: 640px;
    height: 366px;
    border-radius: 4px;
    overflow: hidden;
    box-shadow: 0 6px 18px rgba(0,0,0,0.18);
  }

  /* Back of card */
  .card-back {
    top: 70px;
    background: linear-gradient(180deg, var(--green) 0%, var(--green-light) 100%);
    color: var(--paper);
    text-align: center;
    padding: 52px 56px 0;
  }
  .brand-name {
    font-family: "Lato", sans-serif;
    font-weight: 900;
    text-transform: uppercase;
    letter-spacing: 1px;
    line-height: 1;
  }
  .card-back .brand-name { font-size: 46px; color: var(--paper); }
  .services {
    margin-top: 26px;
    padding: 12px 0;
    border-top: 1px solid rgba(255,255,255,0.7);
    border-bottom: 1px solid rgba(255,255,255,0.7);
    font-size: 15px;
    letter-spacing: 0.5px;
    display: flex;
    justify-content: center;
    gap: 14px;
  }
  .services .divider { opacity: 0.85; }
  .pitch {
    margin-top: 16px;
    font-size: 19px;
    font-weight: 700;
    line-height: 1.3;
  }
  .pitch-note { margin-top: 4px; font-size: 14px; }
  .call-line { margin-top: 4px; font-size: 18px; font-weight: 700; }

  /* Front of card */
  .card-front { top: 464px; background: var(--paper); }
  .card-front .wave { position: absolute; inset: 0; width: 100%; height: 100%; }
  .person {
    position: absolute;
    left: 44px;
    top: 62px;
    font-family: "Arimo", sans-serif;
  }
  .person-name { color: var(--green); font-size: 22px; font-weight: 700; letter-spacing: 0.5px; }
  .person-title { color: var(--grey-text); font-size: 17px; margin-top: 2px; }
  .card-front .brand-name {
    position: absolute;
    right: 40px;
    top: 58px;
    width: 270px;
    font-size: 40px;
    color: var(--green-deep);
    text-align: left;
  }
  .contacts {
    position: absolute;
    left: 44px;
    top: 230px;
    list-style: none;
    font-family: "Arimo", sans-serif;
    font-size: 17px;
    color: var(--ink);
  }
  .contacts li { display: flex; align-items: center; gap: 8px; margin-bottom: 6px; }
  .contacts svg { width: 14px; height: 14px; fill: var(--green); flex: none; }
</style>
</head>
<body>

  <section class="card card-back" aria-label="Back of business card">
    <h1 class="brand-name">Renewed Residences</h1>
    <p class="services">
      <span>BUY A HOME</span><span class="divider">|</span>
      <span>FACING FORECLOSURE</span><span class="divider">|</span>
      <span>SELL A HOME</span>
    </p>
    <p class="pitch">We are a group of Real Estate Investors that are<br>looking to buy and sell homes in your area.</p>
    <p class="pitch-note">If you are buying or selling a home in Illinois we want to talk to you.</p>
    <p class="call-line">Call Us Now 555-014-SOLD</p>
  </section>

  <section class="card card-front" aria-label="Front of business card">
    <svg class="wave" viewBox="0 0 640 366" preserveAspectRatio="none" aria-hidden="true">
      <path d="M0 332 C 200 392 430 300 640 168 L640 180 C 430 318 200 404 0 348 Z" fill="var(--ink)"/>
      <path d="M0 350 C 200 404 430 320 640 180 L640 366 L0 366 Z" fill="var(--green)"/>
    </svg>
    <div class="person">
      <p class="person-name">DANIEL HART</p>
      <p class="person-title">Managing Director</p>
    </div>
    <p class="brand-name">Renewed Residences</p>
    <ul class="contacts">
      <li>
        <svg viewBox="0 0 24 24"><path d="M6.6 10.8a15 15 0 0 0 6.6 6.6l2.2-2.2a1 1 0 0 1 1-.25 11.4 11.4 0 0 0 3.6.57 1 1 0 0 1 1 1V20a1 1 0 0 1-1 1A17 17 0 0 1 3 4a1 1 0 0 1 1-1h3.5a1 1 0 0 1 1 1c0 1.25.2 2.45.57 3.57a1 1 0 0 1-.25 1z"/></svg>
        555-014-SOLD
      </li>
      <li>
        <svg viewBox="0 0 24 24"><path d="M2 5h20v14H2z M4 7v.5l8 5 8-5V7l-8 5z" fill-rule="evenodd"/></svg>
        hello@renewedresidences.com
      </li>
      <li>
        <svg viewBox="0 0 24 24"><circle cx="12" cy="12" r="10"/></svg>
        www.quickdeedhomestead.com
      </li>
    </ul>
  </section>

</body>
</html>
```